BRELLANDA EXTRA VIRGIN OLIVE OIL

I needs a design for an Australian Extra Virgin Olive Oil.

The label will go on a round clear bottle

The label size front and back is 145mm high x 60mm wide.

The important points for the design are as follows.

I want to see elegant olives on the label so that non English speaking markets can easily understand its olive oil. I want it too look classy . IT must also look Australian but I don't want to see kangaroos just colours that reflect Australia.

The mandatory info on front label will be

BRELLANDA

Cold Pressed
EXTRA VIRGIN OLIVE OIL

AUSTRALIAN

1 litre

```html
<!DOCTYPE html>
<html lang="en">
<head>
<meta charset="utf-8">
<title>Brellanda Extra Virgin Olive Oil – Front Label</title>
<link rel="stylesheet" href="https://fonts.googleapis.com/css2?family=Cinzel:wght@400;600&family=Libre+Baskerville:wght@400&display=swap">
<style>
  :root {
    --canvas: #ffffff;
    --label-yellow: #f6c226;
    --panel-black: #15160f;
    --rule-green: #2f9a3a;
    --title-red: #b3151c;
    --brand-gold: #f6c226;
    --cream: #f4efe0;
    --olive-deep: #2f4a1c;
    --olive-light: #8aa23a;
  }
  html, body {
    margin: 0;
    width: 882px;
    height: 1200px;
    overflow: hidden;
    background: var(--canvas);
  }
  .label {
    position: absolute;
    left: 121px;
    top: 55px;
    width: 640px;
    height: 1090px;
    border-radius: 30px;
    overflow: hidden;
    background: var(--label-yellow);
  }
  .label-shapes {
    position: absolute;
    inset: 0;
  }
  .label-text {
    position: absolute;
    left: 0;
    width: 100%;
    margin: 0;
    text-align: center;
  }
  .brand {
    top: 225px;
    font-family: "Cinzel", serif;
    font-weight: 600;
    font-size: 60px;
    line-height: 70px;
    letter-spacing: 2px;
    color: var(--brand-gold);
  }
  .method {
    top: 345px;
    font-family: "Libre Baskerville", serif;
    font-size: 30px;
    line-height: 40px;
    letter-spacing: 1px;
    color: var(--cream);
  }
  .product-name {
    top: 492px;
    font-family: "Libre Baskerville", serif;
    font-size: 64px;
    line-height: 74px;
    letter-spacing: 1px;
    color: var(--title-red);
  }
  .origin {
    top: 952px;
    font-family: "Cinzel", serif;
    font-weight: 600;
    font-size: 20px;
    line-height: 22px;
    letter-spacing: 6px;
    color: var(--brand-gold);
  }
  .volume {
    top: 1000px;
    font-family: "Libre Baskerville", serif;
    font-size: 28px;
    line-height: 36px;
    color: var(--panel-black);
  }
  .olive-illustration {
    position: absolute;
    left: 150px;
    top: 742px;
    width: 340px;
    height: 176px;
    border-radius: 12px;
    background: radial-gradient(ellipse at 40% 45%, #c9a533 0%, var(--olive-light) 40%, var(--olive-deep) 80%, var(--panel-black) 100%);
  }
</style>
</head>
<body>
  <div class="label">
    <svg class="label-shapes" width="640" height="1090" viewBox="0 0 640 1090" aria-hidden="true">
      <rect x="0" y="0" width="640" height="38" fill="var(--panel-black)"/>
      <rect x="0" y="38" width="640" height="4" fill="var(--rule-green)"/>
      <path d="M50,470 V235 C50,175 200,165 262,125 Q300,100 320,72 Q340,100 378,125 C440,165 590,175 590,235 V470 Z"
            fill="var(--panel-black)" stroke="var(--rule-green)" stroke-width="5"/>
      <line x1="150" y1="315" x2="490" y2="315" stroke="var(--rule-green)" stroke-width="3"/>
      <circle cx="320" cy="315" r="6" fill="var(--rule-green)"/>
      <line x1="50" y1="478" x2="590" y2="478" stroke="var(--rule-green)" stroke-width="5"/>
      <line x1="50" y1="722" x2="590" y2="722" stroke="var(--rule-green)" stroke-width="5"/>
      <rect x="50" y="730" width="540" height="200" fill="var(--panel-black)" stroke="var(--rule-green)" stroke-width="5"/>
      <rect x="50" y="946" width="540" height="32" fill="var(--panel-black)"/>
      <line x1="50" y1="944" x2="590" y2="944" stroke="var(--rule-green)" stroke-width="3"/>
      <line x1="50" y1="982" x2="590" y2="982" stroke="var(--rule-green)" stroke-width="3"/>
    </svg>

    <p class="label-text brand">BRELLANDA</p>
    <p class="label-text method">COLD<br>PRESSED</p>
    <p class="label-text product-name">EXTRA<br>VIRGIN<br>OLIVE OIL</p>

    <div class="olive-illustration" role="img" aria-label="Illustration of an olive oil jug with a sprig of green olives and leaves"></div>

    <p class="label-text origin">AUSTRALIAN</p>
    <p class="label-text volume">1 litre</p>
  </div>
</body>
</html>
```